Beautiful Upgraded Single Story Home in Brindlemere...SOLD in 3 days for top $$!

This is a 6.5" x 11" EDDM postcard. Please use the indicia files and 6.5" x 11" template attached in the brief.
Updates

Project Deadline Extended
Reason: We are still working on the details for one of the postcards. Thanks

Target Market(s)

Listings

Font styles to use
Serif

Colors
33b8a4

Requirements
Must have
• Call me if you are interested in getting the most amount of equity out of your home!
• Marisol Pendry (555) 417-2963 and Tamsin Okavell (555) 730-4186
• Marisol@TeamOkavell.example and Tamsin@TeamOkavell.example
• Harbor Ridge Homes
• The Key to your Real Estate Needs!
• (At bottom of postcard) "If you are currently listed with a licensed Realtor, this is not intended as solicitation"
Nice to have
• The Front Should be the Property Picture and "In Escrow in 3 Days!"

```html
<!DOCTYPE html>
<html lang="en">
<head>
<meta charset="utf-8">
<title>Brindlemere Postcard</title>
<link rel="stylesheet" href="https://fonts.googleapis.com/css2?family=Cormorant+Garamond:ital,wght@1,500;1,600&family=Libre+Baskerville:wght@400;700&display=swap">
<style>
:root{
  --teal:#33b8a4;
  --ink:#231f20;
  --paper:#ffffff;
  --stage:#e6e7e9;
}
*{box-sizing:border-box;margin:0;padding:0}
html,body{width:1030px;height:1200px;overflow:hidden;background:var(--stage)}
body{position:relative;font-family:"Libre Baskerville",Georgia,serif;color:var(--paper)}
.card{position:absolute;left:80px;width:870px;height:514px;overflow:hidden;background:var(--paper);box-shadow:0 1px 4px rgba(0,0,0,.25)}
.front{top:66px}
.back{top:620px}
.nowrap{white-space:nowrap}
.ico{display:inline-block;width:8px;height:8px;margin-right:4px;vertical-align:-1px}

/* brand name chip */
.brand-chip{position:absolute;width:74px;height:32px;background:var(--paper);color:var(--ink);
  font-size:8px;font-weight:700;line-height:10px;text-align:center;display:flex;align-items:center;justify-content:center;padding:0 6px}

/* front */
.property-photo{position:absolute;left:0;top:0;width:870px;height:461px;
  background:linear-gradient(180deg,#a9c6e6 0%,#cfdcea 40%,#8b7a62 55%,#6f8a3c 75%,#c9c7c0 100%)}
.escrow-banner{position:absolute;left:694px;top:0;width:165px;height:148px;background:var(--teal);
  clip-path:polygon(0 0,100% 0,100% 84%,50% 100%,0 84%);color:var(--ink)}
.escrow-banner .label{position:absolute;top:21px;right:12px;font-size:15px;white-space:nowrap}
.escrow-banner .rule{position:absolute;top:42px;left:14px;right:12px;height:3px;background:var(--ink)}
.escrow-banner .rule::before{content:"";position:absolute;left:0;top:-6px;width:15px;height:15px;border-radius:50%;background:var(--ink)}
.escrow-banner .count{position:absolute;top:50px;left:0;right:0;text-align:center;font-family:"Cormorant Garamond",serif;font-style:italic;font-weight:500;color:var(--paper);font-size:26px;white-space:nowrap}
.escrow-banner .count b{font-size:74px;font-weight:500;vertical-align:-14px;margin-right:4px}
.front-footer{position:absolute;left:0;top:461px;width:870px;height:53px;background:var(--ink)}
.front-brand{left:10px;top:11px}
.tagline{position:absolute;left:90px;top:14px;font-family:"Cormorant Garamond",serif;font-style:italic;font-weight:600;color:var(--teal);font-size:20px;white-space:nowrap}
.agent-inline{position:absolute;top:12px;display:flex;align-items:center;font-size:8.5px;white-space:nowrap}
.agent-inline .name{font-weight:700;padding-right:5px;border-right:1px solid var(--paper);height:30px;display:flex;align-items:center}
.agent-inline .lines{padding-left:5px;line-height:15px}
.front-agent-a{left:360px}
.front-agent-b{left:614px}

/* back */
.back-panel{position:absolute;inset:0;background:var(--ink);clip-path:polygon(0 0,550px 0,444px 514px,0 514px)}
.back-edge{position:absolute;inset:0;background:var(--teal);clip-path:polygon(550px 0,556px 0,450px 514px,444px 514px)}
.sold-tag{position:absolute;left:0;top:48px;width:378px;height:40px;background:var(--teal);font-size:21px;font-weight:700;padding:8px 0 0 11px;white-space:nowrap}
.headline{position:absolute;left:12px;top:98px;font-family:"Cormorant Garamond",serif;font-style:italic;font-weight:500;font-size:45px;line-height:58px;white-space:nowrap}
.photo-frame{position:absolute;left:10px;top:260px;width:188px;height:220px;border:1px solid #888}
.agents-photo{position:absolute;left:15px;top:247px;width:187px;height:228px;
  background:linear-gradient(160deg,#4d7f76 0%,#b9a58f 45%,#2c2a2b 80%)}
.contact{position:absolute;left:150px;top:250px;width:320px;text-align:right}
.contact h2{color:var(--teal);font-size:14px;font-weight:700}
.contact p{font-family:"Cormorant Garamond",serif;font-style:italic;font-weight:600;color:var(--teal);font-size:16px;line-height:18px;margin-top:2px;white-space:nowrap}
.contact-rule{position:absolute;left:212px;top:308px;width:258px;height:3px;background:var(--paper)}
.contact-rule::before{content:"";position:absolute;left:0;top:-8px;width:18px;height:18px;border-radius:50%;background:var(--paper)}
.agent-card{position:absolute;left:190px;display:flex;align-items:center;font-size:9px;white-space:nowrap}
.agent-card .name{width:112px;text-align:right;justify-content:flex-end;font-weight:700;padding-right:6px;border-right:1px solid var(--paper);height:48px;display:flex;align-items:center}
.agent-card .lines{padding-left:6px;line-height:15px}
.agent-a{top:328px}
.agent-b{top:383px}
.back-brand{left:299px;top:441px}
.disclaimer{position:absolute;left:13px;top:489px;font-family:"Cormorant Garamond",serif;font-style:italic;font-weight:600;font-size:11px;white-space:nowrap}
.indicia{position:absolute;left:799px;top:11px;width:62px;height:60px;border:1px solid var(--ink);color:var(--ink);font-family:Arial,sans-serif;font-size:8px;line-height:10px;text-align:center;padding-top:4px;white-space:nowrap}
.address-box{position:absolute;left:661px;top:393px;width:199px;height:79px;border:1px solid var(--ink);color:var(--ink);font-family:Arial,sans-serif;font-size:12px;padding:10px 14px;line-height:13px}
.address-box .route{text-align:right;font-size:10px;margin-bottom:16px}
</style>
</head>
<body>

<section class="card front">
  <div class="property-photo" role="img" aria-label="Photo of the single story home with front lawn, tree and driveway"></div>
  <div class="escrow-banner">
    <div class="label">IN ESCROW IN</div>
    <div class="rule"></div>
    <div class="count"><b>3</b>days</div>
  </div>
  <footer class="front-footer">
    <div class="brand-chip front-brand">Harbor Ridge Homes</div>
    <div class="tagline">The Key to your Real Estate Needs!</div>
    <div class="agent-inline front-agent-a">
      <span class="name">MARISOL PENDRY</span>
      <span class="lines">
        <svg class="ico" viewBox="0 0 10 10"><path d="M2 1l2 2-1 1.5c.8 1.4 1.8 2.4 3 3L7.5 6l2 2-1.5 1.5C4 9 1 5.5.5 2.5z" fill="#33b8a4"/></svg>(555) 417-2963<br>
        <svg class="ico" viewBox="0 0 10 10"><rect x="0" y="2" width="10" height="6" fill="#33b8a4"/></svg>Marisol@TeamOkavell.example
      </span>
    </div>
    <div class="agent-inline front-agent-b">
      <span class="name">TAMSIN OKAVELL</span>
      <span class="lines">
        <svg class="ico" viewBox="0 0 10 10"><path d="M2 1l2 2-1 1.5c.8 1.4 1.8 2.4 3 3L7.5 6l2 2-1.5 1.5C4 9 1 5.5.5 2.5z" fill="#33b8a4"/></svg>(555) 730-4186<br>
        <svg class="ico" viewBox="0 0 10 10"><rect x="0" y="2" width="10" height="6" fill="#33b8a4"/></svg>Tamsin@TeamOkavell.example
      </span>
    </div>
  </footer>
</section>

<section class="card back">
  <div class="back-panel"></div>
  <div class="back-edge"></div>
  <div class="sold-tag">SOLD in 3 days above list price!</div>
  <h1 class="headline">Beautiful Upgraded Single<br>Story Home in Brindlemere...</h1>
  <div class="photo-frame"></div>
  <div class="agents-photo" role="img" aria-label="Portrait of the two agents"></div>
  <div class="contact">
    <h2>CONTACT US</h2>
    <p>if you are interested in getting the most<br>amount of equity out of your home!</p>
  </div>
  <div class="contact-rule"></div>
  <div class="agent-card agent-a">
    <span class="name">MARISOL PENDRY</span>
    <span class="lines">
      <svg class="ico" viewBox="0 0 10 10"><path d="M2 1l2 2-1 1.5c.8 1.4 1.8 2.4 3 3L7.5 6l2 2-1.5 1.5C4 9 1 5.5.5 2.5z" fill="#33b8a4"/></svg>(555) 417-2963<br>
      <svg class="ico" viewBox="0 0 10 10"><rect x="0" y="2" width="10" height="6" fill="#33b8a4"/></svg>Marisol@TeamOkavell.example<br>
      <svg class="ico" viewBox="0 0 10 10"><path d="M1 5l3 3 5-6" stroke="#33b8a4" stroke-width="2" fill="none"/></svg>BRE #04812736
    </span>
  </div>
  <div class="agent-card agent-b">
    <span class="name">TAMSIN OKAVELL</span>
    <span class="lines">
      <svg class="ico" viewBox="0 0 10 10"><path d="M2 1l2 2-1 1.5c.8 1.4 1.8 2.4 3 3L7.5 6l2 2-1.5 1.5C4 9 1 5.5.5 2.5z" fill="#33b8a4"/></svg>(555) 730-4186<br>
      <svg class="ico" viewBox="0 0 10 10"><rect x="0" y="2" width="10" height="6" fill="#33b8a4"/></svg>Tamsin@TeamOkavell.example<br>
      <svg class="ico" viewBox="0 0 10 10"><path d="M1 5l3 3 5-6" stroke="#33b8a4" stroke-width="2" fill="none"/></svg>BRE #06295148
    </span>
  </div>
  <div class="brand-chip back-brand">Harbor Ridge Homes</div>
  <p class="disclaimer">If you are currently listed with a licensed Realtor, this is not intended as solicitation.</p>
  <div class="indicia">PRSRT STD<br>ECRWSS<br>U.S. Postage<br><b>PAID</b><br>EDDM RETAIL</div>
  <div class="address-box">
    <div class="route">******************ECRWSS****</div>
    Local<br>Postal Customer
  </div>
</section>

</body>
</html>
```